Finch Haulage Ltd

We need an A5 size (UK size) flyer to advertise our new business which is called Finch Haulage.
Domestic and Commercial Waste Clearance Services.
Please have the question in bold "Do you have a pile of junk you need to dispose of?"
We collect all kinds of junk or rubbish from homes and businesses across Kent, Sussex and South London.
No fuss, no mess!
A low cost, hassle free alternative to skip hire.
Licensed by the Landcare Board and fully insured (this can be in small print at the bottom).
Please put the Recycle symbol somewhere.
Our tagline on our vehicle is "We Clear More, For Less!"
We'd like the flyer to be bold and eye-catching (to catch the eye of the homeowner or business owner while it's sitting on their doormat).
We need our telephone, website and email to be prominent. Maybe saying "Call today for a free quote"
Tel. 01734 586019
Email: info@finchhaulage.example.co.uk
www.finchhaulage.example.co.uk
Target Market(s)
Our market will be homes and small businesses around Kent, Sussex and South London.

```html
<!DOCTYPE html>
<html lang="en">
<head>
<meta charset="utf-8">
<title>Finch Haulage – Waste Clearance Flyer</title>
<link rel="stylesheet" href="https://fonts.googleapis.com/css2?family=Arimo:wght@400;700&family=League+Gothic&family=Oswald:wght@300;400;500;600;700&family=Roboto+Condensed:ital,wght@0,300;0,700;1,300&display=swap">
<style>
  :root {
    --ink: #2b2b2b;
    --ink-soft: #4d4d4d;
    --muted: #7a7a7a;
    --panel-grey: #d9d9d9;
    --panel-light: #f4f4f4;
    --side-grey: #f1f1f1;
    --white: #ffffff;
    --brand-green: #2db34a;
    --band-green: #b2dba6;
    --icon-green: #a8d7a0;
    --junk-dark: #4f4741;
    --junk-mid: #7d7670;
    --junk-warm: #8a5a3c;
  }
  * { box-sizing: border-box; margin: 0; padding: 0; }
  html, body { width: 852px; height: 1200px; overflow: hidden; background: var(--white); }
  .flyer {
    position: relative;
    width: 852px;
    height: 1200px;
    font-family: "Arimo", Arial, sans-serif;
    color: var(--ink);
    background: var(--white);
  }
  .fit-text { position: absolute; left: 0; top: 0; overflow: visible; }

  /* Headline question */
  .question {
    position: absolute; left: 0; top: 0;
    width: 852px; height: 374px;
    background: var(--panel-grey);
  }
  .question h1 { font-weight: normal; }
  .licence-note {
    position: absolute; right: 38px; top: 26px;
    font-size: 17px; color: var(--muted);
  }
  .headline-lead, .headline-tail {
    font-family: "League Gothic", "Oswald", sans-serif;
    fill: var(--ink);
  }
  .headline-main {
    font-family: "League Gothic", "Oswald", sans-serif;
  }

  /* Brand band */
  .brand-band {
    position: absolute; left: 0; top: 374px;
    width: 852px; height: 206px;
    background: var(--white);
  }
  .brand-band::before, .brand-band::after {
    content: ""; position: absolute; top: 0; width: 172px; height: 100%;
    background: var(--side-grey);
  }
  .brand-band::before { left: 0; }
  .brand-band::after { right: 0; }
  .brand-mark {
    position: absolute; left: 200px; top: 86px;
    width: 30px; height: 30px; border-radius: 50%;
    background: var(--brand-green);
  }
  .brand-name {
    font-family: "Oswald", sans-serif; font-weight: 700;
    fill: var(--ink-soft);
  }

  /* Services */
  .services {
    position: absolute; left: 0; top: 580px;
    width: 852px; height: 374px;
    background: linear-gradient(180deg, #dcdcdc 0%, var(--panel-light) 100%);
  }
  .service-lines {
    position: absolute; left: 0; top: 32px; width: 864px;
    text-align: center;
    font-size: 30px; line-height: 39px;
    color: var(--ink);
  }
  .service-lines strong {
    font-family: "Roboto Condensed", sans-serif; font-weight: 700;
    font-size: 33px;
  }
  .recycle-icon { position: absolute; left: 676px; top: 66px; width: 118px; height: 116px; }
  .tagline {
    font-family: "Oswald", sans-serif; font-weight: 600;
    fill: var(--ink);
  }

  /* Contact band */
  .contact-band {
    position: absolute; left: 0; top: 954px;
    width: 852px; height: 132px;
    background: var(--band-green);
  }
  .call-to-action {
    position: absolute; left: 30px; top: 46px;
    font-family: "Roboto Condensed", sans-serif; font-weight: 300; font-style: italic;
    font-size: 38px; line-height: 1;
    color: var(--ink);
  }
  .contact-arrow { position: absolute; left: 444px; top: 28px; width: 60px; height: 82px; }
  .contact-details { font-style: normal; }
  .phone { font-family: "Oswald", sans-serif; font-weight: 500; fill: var(--ink); }
  .email { font-family: "Oswald", sans-serif; font-weight: 300; fill: var(--ink); }

  /* Website */
  .website {
    position: absolute; left: 0; top: 1086px;
    width: 852px; height: 114px;
    display: flex; align-items: center; justify-content: center;
    font-size: 36px; color: var(--brand-green);
  }
</style>
</head>
<body>
<main class="flyer">
  <section class="question">
    <p class="licence-note">Licensed by the Landcare Board and fully insured</p>
    <h1 aria-label="Do you have a pile of junk you need to dispose of?">
      <svg class="fit-text" width="852" height="374" viewBox="0 0 852 374" aria-hidden="true">
        <defs>
          <linearGradient id="junkFill" x1="0" y1="0" x2="1" y2="0.3">
            <stop offset="0" stop-color="var(--junk-dark)"/>
            <stop offset="0.3" stop-color="var(--junk-mid)"/>
            <stop offset="0.6" stop-color="var(--junk-warm)"/>
            <stop offset="1" stop-color="var(--junk-dark)"/>
          </linearGradient>
        </defs>
        <text class="headline-lead" x="34" y="102" font-size="52" textLength="204" lengthAdjust="spacingAndGlyphs">DO YOU HAVE</text>
        <text class="headline-main" x="37" y="292" font-size="236" fill="url(#junkFill)" textLength="789" lengthAdjust="spacingAndGlyphs">A PILE OF JUNK</text>
        <text class="headline-tail" x="35" y="346" font-size="51" textLength="791" lengthAdjust="spacing">Y O U   N E E D   T O   D I S P O S E   O F ?</text>
      </svg>
    </h1>
  </section>

  <section class="brand-band">
    <span class="brand-mark"></span>
    <svg class="fit-text" width="852" height="206" viewBox="0 0 852 206" role="img" aria-label="Finch Haulage">
      <text class="brand-name" x="246" y="132" font-size="74" textLength="410" lengthAdjust="spacingAndGlyphs">FINCH HAULAGE</text>
    </svg>
  </section>

  <section class="services">
    <p class="service-lines">
      We Collect All Kinds Of Junk Or Rubbish<br>
      From Homes And Business.<br>
      NO FUSS, NO MESS!<br>
      <strong>Very competitive prices!</strong>
    </p>
    <svg class="recycle-icon" viewBox="0 0 120 116" aria-label="Recycle symbol">
      <g fill="var(--icon-green)">
        <path d="M46 6 L72 6 L86 30 L96 24 L90 54 L62 46 L72 40 L60 20 L52 34 L38 26 Z"/>
        <path d="M100 62 L114 86 L100 110 L74 110 L74 122 L56 98 L74 74 L74 86 L98 86 L90 72 Z" transform="translate(0 -8)"/>
        <path d="M36 38 L24 58 L34 64 L4 70 L0 44 L10 50 L22 30 Z"/>
        <path d="M6 80 L40 80 L40 104 L18 104 L4 92 Z"/>
      </g>
    </svg>
    <svg class="fit-text" width="852" height="374" viewBox="0 0 852 374" aria-label="We Clear More, For Less!!!">
      <text class="tagline" x="121" y="314" font-size="68" textLength="624" lengthAdjust="spacingAndGlyphs">We Clear More, For Less!!!</text>
    </svg>
  </section>

  <section class="contact-band">
    <p class="call-to-action">Call today for a free quote!</p>
    <svg class="contact-arrow" viewBox="0 0 60 82" aria-hidden="true">
      <path d="M32 2 C10 8 2 28 10 48 L22 44 C16 30 20 18 34 12 Z" fill="var(--ink)"/>
      <path d="M2 50 L36 38 L40 80 Z" fill="var(--ink)"/>
    </svg>
    <address class="contact-details">
      <svg class="fit-text" width="852" height="132" viewBox="0 0 852 132" aria-label="Telephone 01734 586019, email info@finchhaulage.example.co.uk">
        <text class="phone" x="816" y="74" font-size="62" text-anchor="end" textLength="300" lengthAdjust="spacingAndGlyphs">01734 586019</text>
        <text class="email" x="816" y="110" font-size="30" text-anchor="end" textLength="300" lengthAdjust="spacingAndGlyphs">info@finchhaulage.example.co.uk</text>
      </svg>
    </address>
  </section>

  <footer class="website">www.finchhaulage.example.co.uk</footer>
</main>
</body>
</html>
```